Stationery Design Project for Brindle Co

Hi All,

We need you to design stationary for a new online financial services business. We have already got the logo designed and it is attached. If you would like it in any other formats please let me know. If you could also if possible, match the fonts in your design to that on the logo’s provided.

What we need:
- Business Card
- A4 Letter head
- A4 Folders
- PPT template (Title page and regular page)

And what ever else you want to throw in.

We are in the process of getting the web site designed, however below is a list of websites which we like which will give you an understanding of the style that we are going for.

- plumvale.example
- hobnailworks.example
- grintablet.example
- lumpwillow.example

I look forward to your seeing your design.

• Outputs:
- Documents ready to print
- Generic editable information
- Pdf copies of the documents
- Word version of letterhead

```html
<!DOCTYPE html>
<html lang="en">
<head>
<meta charset="utf-8">
<title>Brindle Co Stationery</title>
<link rel="stylesheet" href="https://fonts.googleapis.com/css2?family=Oswald:wght@300&family=Questrial&display=swap">
<style>
  :root{
    --brand-blue:#1380a9;
    --brand-orange:#f7941e;
    --ink:#444448;
    --label-grey:#8c8c8e;
    --paper:#ffffff;
    --faint:#d6d6d8;
    --faint-orange:#fbdcb8;
    --rule-blue:#5aa6cf;
  }
  *{margin:0;padding:0;box-sizing:border-box}
  html,body{width:1200px;height:900px;overflow:hidden}
  body{
    position:relative;
    background:linear-gradient(#ffffff 0%,#f9f9fa 45%,#eeeef0 100%);
    font-family:"Questrial",sans-serif;
    color:var(--ink);
  }
  .board-label{
    position:absolute;
    font-family:"Oswald",sans-serif;
    font-weight:300;
    font-size:21px;
    line-height:30px;
    color:var(--label-grey);
    letter-spacing:.2px;
  }

  /* wordmark */
  .wordmark{display:flex;align-items:center;white-space:nowrap;font-family:"Questrial",sans-serif}
  .wordmark .dot{border-radius:50%;background:var(--brand-orange);flex:none}

  /* business card */
  .card-front{
    position:absolute;left:177px;top:198px;width:405px;height:95px;
    background:var(--brand-blue);
    display:flex;align-items:center;justify-content:center;
  }
  .card-front .wordmark{color:#fff;font-size:30px;gap:14px}
  .card-front .dot{width:42px;height:42px}

  .card-back{
    position:absolute;left:600px;top:198px;width:405px;height:95px;
    background:var(--paper);border:1px solid var(--brand-blue);
    overflow:hidden;
  }
  .card-back .band-blue{position:absolute;left:324px;top:0;width:58px;height:100%;background:var(--brand-blue)}
  .card-back .band-orange{position:absolute;left:382px;top:0;width:23px;height:100%;background:var(--brand-orange)}
  .card-back .name-line{position:absolute;left:16px;top:10px;font-size:14.5px;letter-spacing:.6px}
  .card-back .name-line .role{margin-left:14px}
  .card-back .contact-line{position:absolute;left:16px;top:33px;font-size:10px;letter-spacing:.3px;word-spacing:1px}
  .card-back .contact-line span+span{margin-left:14px}
  .card-back .address-line{position:absolute;left:16px;top:50px;font-size:10px;letter-spacing:.3px}
  .card-back .wordmark{position:absolute;left:212px;top:71px;font-size:12px;gap:5px;color:var(--ink)}
  .card-back .wordmark .dot{width:14px;height:14px}

  /* letterhead */
  .letterhead-sheet{
    position:absolute;width:330px;height:390px;background:var(--paper);
    border:1px solid var(--rule-blue);
  }
  .letterhead-sheet.under{left:95px;top:382px;box-shadow:1px 1px 3px rgba(0,0,0,.08)}
  .letterhead-sheet.top{left:105px;top:392px;overflow:hidden;box-shadow:1px 2px 4px rgba(0,0,0,.12)}
  .letterhead-sheet.under::after{
    content:"";position:absolute;right:0;top:0;width:18px;height:100%;background:var(--brand-blue);
  }
  .letterhead-sheet .side-strip{
    position:absolute;right:0;top:0;width:18px;height:100%;background:var(--brand-blue);
    color:#fff;font-size:6.5px;letter-spacing:.3px;font-weight:700;
    writing-mode:vertical-rl;
    display:flex;justify-content:space-between;align-items:center;padding:16px 0 14px;
  }
  .letterhead-sheet .side-strip .gap-after{margin-bottom:40px}
  .letterhead-sheet .wordmark.head{position:absolute;right:30px;top:12px;font-size:11px;gap:4px;color:var(--ink)}
  .letterhead-sheet .wordmark.head .dot{width:12px;height:12px}
  .letterhead-sheet .wordmark.ghost{position:absolute;left:12px;bottom:28px;font-size:27px;gap:12px;color:var(--faint)}
  .letterhead-sheet .wordmark.ghost .dot{width:38px;height:38px;background:var(--faint-orange)}

  /* folder */
  .folder-front{
    position:absolute;left:538px;top:420px;width:277px;height:369px;
    background:var(--paper);border:1px solid var(--rule-blue);
  }
  .folder-front .band-orange{position:absolute;left:0;top:93px;width:100%;height:40px;background:var(--brand-orange)}
  .folder-front .cover-panel{
    position:absolute;left:31px;top:33px;width:213px;height:160px;background:var(--brand-blue);
    box-shadow:2px 3px 5px rgba(0,0,0,.25);
    display:flex;align-items:center;justify-content:center;
  }
  .folder-front .cover-panel .wordmark{color:#fff;font-size:17px;gap:8px}
  .folder-front .cover-panel .dot{width:24px;height:24px}
  .folder-back{
    position:absolute;left:828px;top:422px;width:277px;height:368px;
    background:var(--brand-orange);box-shadow:1px 2px 4px rgba(0,0,0,.15);
  }
  .folder-footer{
    position:absolute;left:8px;right:8px;bottom:6px;
    display:flex;justify-content:space-between;
    font-size:5px;letter-spacing:.2px;font-weight:700;white-space:nowrap;
  }
  .folder-front .folder-footer{color:var(--brand-blue)}
  .folder-back .folder-footer{color:#fff3e2}
</style>
</head>
<body>

  <div class="board-label" style="left:179px;top:111px">BUSINESS CARD<br>(LARGER THAN ACTUAL SIZE)</div>

  <section class="card-front">
    <div class="wordmark"><span class="dot"></span><span>brindle.example</span></div>
  </section>

  <section class="card-back">
    <div class="name-line">Mr Alan Pike<span class="role">MANAGING DIRECTOR</span></div>
    <div class="contact-line"><span>T: 07 5550 1234</span><span>M: 020 5550 9876</span><span>E: ap@brindle.example</span></div>
    <div class="address-line">48 TALLOW LANE HARBOURSIDE 3213</div>
    <div class="wordmark"><span class="dot"></span><span>brindle.example</span></div>
    <div class="band-blue"></div>
    <div class="band-orange"></div>
  </section>

  <div class="letterhead-sheet under"></div>
  <section class="letterhead-sheet top">
    <div class="wordmark head"><span class="dot"></span><span>brindle.example</span></div>
    <div class="side-strip">
      <span>48 TALLOW LANE HARBOURSIDE 3213</span>
      <span>E: ap@brindle.example</span>
      <span>M: 020 5550 9876</span>
      <span>T: 07 5550 1234</span>
    </div>
    <div class="wordmark ghost"><span class="dot"></span><span>brindle.example</span></div>
  </section>
  <div class="board-label" style="left:162px;top:811px">A4 LETTERHEAD</div>

  <section class="folder-front">
    <div class="band-orange"></div>
    <div class="cover-panel">
      <div class="wordmark"><span class="dot"></span><span>brindle.example</span></div>
    </div>
    <div class="folder-footer">
      <span>T: 07 5550 1234</span><span>M: 020 5550 9876</span><span>E: ap@brindle.example</span><span>48 TALLOW LANE HARBOURSIDE 3213</span>
    </div>
  </section>

  <section class="folder-back">
    <div class="folder-footer">
      <span>T: 07 5550 1234</span><span>M: 020 5550 9876</span><span>E: ap@brindle.example</span><span>48 TALLOW LANE HARBOURSIDE 3213</span>
    </div>
  </section>
  <div class="board-label" style="left:537px;top:811px">A4 FOLDER - FRONT AND BACK</div>

</body>
</html>
```